Industry automation wholesale website

www.velqora.eu provides solutions for automation, building automation and digital signage.

Our products are rugged, reliable, energy saving and representative.

Scope of pages:
● welcome page
- scope of products
- applications, success stories and news
● category page
- short introduction
- sub categories
- product highlights
● product page
- short introduction
- about 3 to 4 pictures
- technical specifications: materials, dimensions
- price
- related products

Optional:
● contact page
- address
- contact form
● blog
- picture
- text
● logo
● favicon / apple touch icon

Conclusion:
● We need a professionally looking site
● Bright colors (e.g. white, grey, metalic colors, blue)

some pages we like:
http://www.brundafel.de/
http://www.korvimash.de/

Target Market(s)

Our target market is the industrial sector
● Target audience: engineering and IT professionals

Industry/Entity Type

Building

Requirements
Must have
• ● only use free available fonts e.g. Pellor Type Library (http://www.pellortype.com/webfonts)
Should not have
• ● sound
● flash

```html
<!DOCTYPE html>
<html lang="en">
<head>
<meta charset="utf-8">
<title>velqora – analog digital measurements</title>
<link href="https://fonts.googleapis.com/css2?family=Michroma&family=Open+Sans:wght@400;600;700;800&display=swap" rel="stylesheet">
<style>
:root{
  --blue:#1b8fd8;
  --blue-dark:#1a5f93;
  --navy:#10304f;
  --ink:#2a3b4c;
  --grey:#8a8f95;
  --grey-light:#c9ccd0;
  --line:#e3e5e8;
  --dark:#1f1f1f;
  --black:#101010;
  --white:#ffffff;
  --foot-text:#d4d4d4;
}
*{margin:0;padding:0;box-sizing:border-box}
html,body{width:1200px;height:3255px;overflow:hidden}
body{position:relative;background:var(--white);font-family:"Open Sans",Arial,sans-serif;color:var(--ink)}
.abs{position:absolute}
.display{font-family:"Michroma",Arial,sans-serif;font-weight:400}
p{line-height:1.45}

/* header */
.hero{left:0;top:0;width:1200px;height:525px;background:radial-gradient(ellipse at 78% 55%,#7e95a8 0%,#3f5468 30%,#283340 60%,#1a2129 100%)}
.nav-band{left:0;top:0;width:1200px;height:60px;background:rgba(9,36,62,.85)}
.logo-box{left:152px;top:0;width:238px;height:78px;background:var(--white);padding:10px 16px}
.logo-name{font-family:"Open Sans",sans-serif;font-weight:700;font-size:40px;color:var(--blue-dark);line-height:42px;display:flex;align-items:center;gap:10px}
.logo-name i{display:inline-block;width:12px;height:12px;background:var(--blue-dark)}
.logo-tag{font-size:11px;color:var(--blue-dark);letter-spacing:.5px}
.nav{left:620px;top:0;height:60px;display:flex;align-items:stretch}
.nav a{display:block;color:var(--white);font-size:14px;font-weight:600;text-decoration:none;padding:20px 24px 0;height:60px}
.nav a.active{background:var(--white);color:var(--blue);padding:20px 16px 0;margin-right:18px}
.hero-kicker{left:150px;top:206px;color:var(--white);font-size:19px}
.hero-title{left:150px;top:226px;color:var(--white);font-size:36px;font-weight:800}
.hero-list{left:150px;top:282px;list-style:none;color:var(--white);font-size:14px}
.hero-list li{display:flex;align-items:center;gap:12px;height:35px}
.hero-list svg{width:20px;height:20px}
.dots{left:563px;top:494px;display:flex;gap:4px}
.dots span{width:13px;height:13px;border-radius:50%;background:var(--blue)}
.dots span.on{background:var(--white)}

/* welcome */
.section-title{font-family:"Michroma",sans-serif;font-size:26px;color:var(--navy);text-transform:lowercase}
.title-rule{height:34px}
.welcome-title{left:152px;top:566px}
.scope-head{left:152px;top:634px;font-size:16px;font-weight:700;color:var(--ink)}
.scope-lead{left:152px;top:666px;width:560px;font-size:11px;color:var(--grey)}
.scope-photo{left:152px;top:690px;width:213px;height:187px;background:linear-gradient(135deg,#6f7478,#b9b4aa 45%,#a04a3c 75%,#5a5d60)}
.scope-text{left:395px;top:692px;width:325px;font-size:11px;color:var(--grey)}
.scope-text p+p{margin-top:6px}
.btn{display:flex;align-items:center;justify-content:center;gap:8px;color:var(--white);font-size:13px;font-weight:600;background:var(--blue);border-radius:2px}
.read-more{left:395px;top:842px;width:100px;height:26px}
.tabs{left:764px;top:575px;width:286px;height:302px;border:1px solid var(--line);box-shadow:0 1px 4px rgba(0,0,0,.12)}
.tab-row{display:flex;height:50px}
.tab-row span{display:flex;align-items:center;justify-content:center;font-size:12px;color:var(--white);background:var(--navy);flex:1;border-left:1px solid #2e5478}
.tab-row span.current{background:var(--white);color:var(--ink);flex:0 0 62px;border:0}
.news{padding:12px 18px 0}
.news-item{padding:10px 0 12px;border-bottom:1px solid var(--line)}
.news-item h4{font-size:12px;font-weight:600;color:var(--blue)}
.news-item p{font-size:10px;color:var(--grey);line-height:1.3;margin-top:2px}
.news-item small{font-size:9px;color:var(--grey);display:block;margin-top:4px}
.cal-btn{margin:14px 0 0 0;width:136px;height:30px;background:var(--navy);color:var(--white);font-size:11px;display:flex;align-items:center}
.cal-btn span{flex:1;text-align:center}
.cal-btn b{width:36px;height:30px;display:flex;align-items:center;justify-content:center;border-left:1px solid #3b6189}

/* category */
.category{left:0;top:950px;width:1200px;height:482px;background:linear-gradient(90deg,#163d68 0%,#24588e 45%,#1d4c7f 75%,#2c659c 100%)}
.center-title{left:0;width:1200px;display:flex;justify-content:center}
.cat-title{top:988px}
.cat-title .section-title{color:var(--white)}
.cat-intro{left:230px;top:1062px;width:740px;text-align:center;color:var(--white);font-size:11px}
.cat-card{top:1146px;width:254px;height:228px;background:var(--white);border-radius:3px;padding:18px}
.cat-card div{width:100%;height:100%}
.arrow{top:1228px;width:40px;height:60px}

/* product */
.prod-title{top:1484px}
.prod-intro{left:230px;top:1553px;width:740px;text-align:center;color:var(--grey-light);font-size:11px}
.prod-highlight{left:436px;top:1610px;width:326px;height:484px;background:var(--blue)}
.prod{top:1660px;width:326px;text-align:center}
.prod .disc{width:240px;height:240px;border-radius:50%;margin:0 auto;background:var(--white);box-shadow:2px 3px 6px rgba(0,0,0,.18);display:flex;align-items:center;justify-content:center}
.prod .disc div{width:170px;height:110px;border-radius:8px}
.prod h3{font-size:17px;font-weight:700;color:var(--blue-dark);margin-top:28px}
.prod p{font-size:11px;color:var(--grey);width:170px;margin:6px auto 0;line-height:1.35}
.prod .price{font-size:18px;color:var(--blue-dark);margin-top:10px}
.prod .btn{width:198px;height:24px;margin:14px auto 0;border-radius:12px;font-weight:400}
.prod.featured h3,.prod.featured p,.prod.featured .price{color:var(--white)}
.prod.featured .btn{background:var(--white);color:var(--blue)}
.top-tab{left:48px;top:2022px;width:34px;height:50px;background:var(--blue)}

/* contact */
.contact{left:0;top:2166px;width:1200px;height:531px;background:radial-gradient(ellipse at 50% 30%,#2c2c2c,#191919 80%)}
.contact-title{left:420px;top:2198px;font-size:50px;color:var(--white)}
.field{background:var(--white);border:1px solid #c8c8c8;font-size:11px;color:#555;padding:0 10px;display:flex;align-items:center}
.field.area{align-items:flex-start;padding-top:10px}
.send{left:154px;top:2580px;width:104px;height:41px}
.info{left:816px;color:var(--white)}
.info h4{font-size:16px;font-weight:700}
.info p{font-size:13px;line-height:1.95;color:#e7e7e7}
.quote{left:816px;top:2580px;width:189px;height:41px}

/* blogs */
.blog-title{top:2724px;color:var(--grey);font-size:20px}
.post{top:2766px;display:flex;gap:26px}
.avatar{width:84px;height:84px;border-radius:50%;border:3px solid var(--white);box-shadow:0 1px 4px rgba(0,0,0,.3);background:linear-gradient(160deg,#9fb4c6,#c79a86 50%,#5b6e80);margin-top:68px;flex:none}
.post h4{font-size:12px;color:var(--blue);font-weight:600}
.post small{font-size:10px;color:var(--grey-light);font-style:italic}
.post p{font-size:11px;color:var(--grey);width:270px;margin-top:6px;line-height:1.4}
.post-divider{left:599px;top:2770px;width:1px;height:180px;background:var(--line)}
.view-all{left:948px;top:2923px;width:102px;height:30px;background:#3a3a3a;font-size:11px}

/* footer */
.footer{left:0;top:2990px;width:1200px;height:265px;background:var(--black)}
.foot-head{font-family:"Michroma",sans-serif;font-size:14px;color:var(--white);text-transform:lowercase}
.sitemap{left:152px;top:3040px;color:var(--foot-text)}
.sitemap ul{list-style:none;margin-top:12px;font-size:11px;line-height:20px}
.map{left:347px;top:3036px;width:278px;height:126px;background:linear-gradient(135deg,#d9d2bf,#efe9da 50%,#c9d3c7)}
.foot-brand{left:649px;top:3046px;color:var(--foot-text)}
.foot-brand .name{font-size:16px;font-weight:700;color:var(--white);display:flex;align-items:center;gap:8px}
.foot-brand .name i{width:8px;height:8px;background:var(--white);display:inline-block}
.foot-line{display:flex;gap:10px;font-size:11px;margin-top:10px;line-height:1.4}
.foot-line svg{flex:none;width:14px;height:14px;margin-top:1px}
.foot-phone{font-size:22px;color:var(--white);margin-top:10px}
.follow{left:907px;top:3040px;color:var(--foot-text)}
.follow ul{list-style:none;margin-top:14px}
.follow li{display:flex;align-items:center;gap:10px;font-size:11px;height:24px}
.follow li i{width:16px;height:16px;background:#555;display:inline-block}
.copy{left:0;top:3198px;width:1200px;border-top:1px solid #2a2a2a;text-align:center;font-size:11px;color:#8d8d8d;padding-top:18px}
</style>
</head>
<body>

<!-- header -->
<header>
  <div class="abs hero" role="img" aria-label="Photo of a hand using a touch panel PC on a stand in an industrial hall"></div>
  <div class="abs nav-band"></div>
  <div class="abs logo-box">
    <div class="logo-name">velqora <i></i></div>
    <div class="logo-tag">analog digital measurements</div>
  </div>
  <nav class="abs nav">
    <a class="active">Home</a><a>Product</a><a>Contact</a><a>Category</a><a>Blog</a>
  </nav>
  <div class="abs hero-kicker">Touch Panel Pc</div>
  <div class="abs hero-title">Bedienterminal</div>
  <ul class="abs hero-list">
    <li><svg viewBox="0 0 20 20"><circle cx="10" cy="10" r="10" fill="#fff"/><path d="M6 10l3 3 5-6" stroke="#10304f" stroke-width="2" fill="none"/></svg>Industrial - IP65 Front • 24/7 Continuous Operation</li>
    <li><svg viewBox="0 0 20 20"><circle cx="10" cy="10" r="10" fill="#fff"/><path d="M6 14l8-8M9 6h5v5" stroke="#10304f" stroke-width="2" fill="none"/></svg>Performance - Corvex Dual Core X410 1,8 GHz</li>
    <li><svg viewBox="0 0 20 20"><circle cx="10" cy="10" r="10" fill="#fff"/><path d="M7 6v8M10 6v8M13 6v8M5 10h10" stroke="#10304f" stroke-width="1.6"/></svg>Fanless - low heat Emission, Power Saving</li>
  </ul>
  <div class="abs dots"><span></span><span class="on"></span><span></span><span></span></div>
</header>

<!-- welcome -->
<section>
  <div class="abs welcome-title">
    <div class="section-title">welcome to velqora</div>
    <svg class="title-rule" width="370" height="20" viewBox="0 0 370 20"><path d="M0 18H364L340 2" stroke="#10304f" stroke-width="1.5" fill="none"/></svg>
  </div>
  <h3 class="abs scope-head">Scope of Products</h3>
  <p class="abs scope-lead">Lorem Ipsum is simply dummy texLorem Ipsum is simply dummy text of the printing and typesetting</p>
  <div class="abs scope-photo" role="img" aria-label="Photo of assorted panel PCs and rugged enclosures"></div>
  <div class="abs scope-text">
    <p>Industry. Lorem Ipsum has been the industry's standard dummy text ever since the when an unknown printer took a galley of type and scrambled it to make a type specimen book. It of the printing and typesetting industry.</p>
    <p>Industry. Lorem Ipsum has been the industry's standard dummy text ever since the when an unknown printer took a galley of type and scrambled it to make a type specimen book. It of the printing and typesetting industry.</p>
  </div>
  <div class="abs btn read-more">Read more</div>

  <aside class="abs tabs">
    <div class="tab-row"><span class="current">News</span><span>Applicatioans</span><span>Success stori</span></div>
    <div class="news">
      <div class="news-item">
        <h4>Lorem Ipsum has been</h4>
        <p>industry's standard dummy text ever since the when a galley of type</p>
        <small>Posted 8/01/14 &nbsp;|&nbsp; Read more ›</small>
      </div>
      <div class="news-item">
        <h4>Lorem Ipsum has been</h4>
        <p>industry's standard dummy text ever since the when a galley of type</p>
        <small>Posted 8/01/14 &nbsp;|&nbsp; Read more ›</small>
      </div>
      <div class="cal-btn"><span>View Calendar</span><b><svg width="14" height="14" viewBox="0 0 14 14"><rect x="1" y="3" width="12" height="10" fill="none" stroke="#fff" stroke-width="1.4"/><path d="M1 6h12M4 1v3M10 1v3" stroke="#fff" stroke-width="1.4"/></svg></b></div>
    </div>
  </aside>
</section>

<!-- category -->
<section>
  <div class="abs category" role="img" aria-label="Blurred blue photo of an industrial workspace"></div>
  <div class="abs center-title cat-title">
    <div style="position:relative">
      <div class="section-title" style="text-align:center;padding-bottom:4px">category</div>
      <svg width="300" height="22" viewBox="0 0 300 22" style="display:block"><path d="M0 20H296L272 2" stroke="#fff" stroke-width="1.5" fill="none"/></svg>
    </div>
  </div>
  <p class="abs cat-intro">Lorem Ipsum is simply dummy texLorem Ipsum is simply dummy text of the printing and typesetting industry. Lorem Ipsum has been the industry's standard dummy text ever since the when an unknown printer took a galley of type and scrambled it to make a type specimen book. It of the printing and typesetting industry.</p>
  <svg class="abs arrow" style="left:122px" viewBox="0 0 40 60"><path d="M34 8L10 30l24 22" stroke="#fff" stroke-width="4" fill="none"/></svg>
  <div class="abs cat-card" style="left:189px"><div role="img" aria-label="Photo of an industrial test chamber" style="background:linear-gradient(135deg,#e9eaec,#b8bcc0 50%,#eef0f2)"></div></div>
  <div class="abs cat-card" style="left:473px"><div role="img" aria-label="Photo of a rugged tablet computer" style="background:linear-gradient(135deg,#5d5f61,#3d6d93 50%,#4a4c4e)"></div></div>
  <div class="abs cat-card" style="left:757px"><div role="img" aria-label="Photo of cockpit display instruments" style="background:linear-gradient(135deg,#3a3c3e,#5e7e6a 50%,#2c2e30)"></div></div>
  <svg class="abs arrow" style="left:1040px" viewBox="0 0 40 60"><path d="M6 8l24 22L6 52" stroke="#fff" stroke-width="4" fill="none"/></svg>
</section>

<!-- product -->
<section>
  <div class="abs center-title prod-title">
    <div>
      <div class="section-title" style="color:var(--blue);text-align:center;padding-bottom:4px">product</div>
      <svg width="300" height="22" viewBox="0 0 300 22" style="display:block"><path d="M0 20H296L272 2" stroke="#1b8fd8" stroke-width="1.5" fill="none"/></svg>
    </div>
  </div>
  <p class="abs prod-intro">Lorem Ipsum is simply dummy texLorem Ipsum is simply dummy text of the printing and typesetting industry. Lorem Ipsum has been the industry's standard dummy text ever since the when an unknown printer took a galley of type and scrambled it to make a type specimen book. It of the printing and typesetting industry.</p>
  <div class="abs prod-highlight"></div>

  <div class="abs prod" style="left:119px">
    <div class="disc"><div role="img" aria-label="Photo of a network router" style="background:linear-gradient(135deg,#3c3e40,#8a8d90 60%,#2f3133);height:50px"></div></div>
    <h3>Technical Specifications</h3>
    <p>Lorem Ipsum is simply dummy texLorem Ipsum is simply dummy text of the printing</p>
    <div class="price">$ 250</div>
    <div class="btn">View More</div>
  </div>
  <div class="abs prod featured" style="left:436px">
    <div class="disc"><div role="img" aria-label="Photo of a touch panel PC" style="background:linear-gradient(135deg,#2c2e30,#5d9a6f 50%,#c24a4a 80%,#2c2e30)"></div></div>
    <h3>Materials</h3>
    <p>Lorem Ipsum is simply dummy texLorem Ipsum is simply dummy text of the printing</p>
    <div class="price">$ 650</div>
    <div class="btn">View More <svg width="12" height="12" viewBox="0 0 12 12" style="margin-left:50px"><circle cx="6" cy="6" r="5" fill="none" stroke="#1b8fd8"/><path d="M5 3.5L7.5 6 5 8.5" stroke="#1b8fd8" fill="none"/></svg></div>
  </div>
  <div class="abs prod" style="left:755px">
    <div class="disc"><div role="img" aria-label="Photo of two smartphones" style="background:linear-gradient(135deg,#1e1f21,#6a7c8c 50%,#1e1f21);width:110px;height:140px"></div></div>
    <h3>Dimensions</h3>
    <p>Lorem Ipsum is simply dummy texLorem Ipsum is simply dummy text of the printing</p>
    <div class="price">$ 450</div>
    <div class="btn">View More</div>
  </div>
  <div class="abs top-tab"></div>
</section>

<!-- contact -->
<section>
  <div class="abs contact"></div>
  <div class="abs display contact-title">contact</div>
  <svg class="abs" style="left:420px;top:2264px" width="370" height="26" viewBox="0 0 370 26"><path d="M0 24H366L340 4" stroke="#fff" stroke-width="1.5" fill="none"/></svg>
  <div class="abs field" style="left:152px;top:2328px;width:262px;height:33px">First Name*</div>
  <div class="abs field" style="left:430px;top:2328px;width:264px;height:33px">Email*</div>
  <div class="abs field" style="left:152px;top:2391px;width:262px;height:33px">Contact Phone No*</div>
  <div class="abs field" style="left:430px;top:2391px;width:264px;height:33px">Subject*</div>
  <div class="abs field area" style="left:152px;top:2452px;width:542px;height:104px">Message*</div>
  <div class="abs btn send">Send <svg width="14" height="14" viewBox="0 0 14 14"><path d="M1 7L13 1 10 13 7 8z" fill="#fff"/></svg></div>

  <div class="abs info" style="top:2312px">
    <h4>Location</h4>
    <p style="width:160px;margin:10px 0 0 4px;line-height:1.95">It has roots in a piece of classical Latin literature from 45 BC</p>
  </div>
  <div class="abs info" style="top:2442px">
    <h4>Contact</h4>
    <p style="margin-top:6px">Phone: 310-482-7715 (Tomas)<br>Email: enquiries@velqora.eu</p>
  </div>
  <div class="abs btn quote">Request Quote <svg width="16" height="14" viewBox="0 0 16 14"><path d="M2 1h10a2 2 0 012 2v4a2 2 0 01-2 2H7l-4 3V9H2z" fill="#fff"/></svg></div>
</section>

<!-- blogs -->
<section>
  <div class="abs center-title blog-title">
    <div style="display:flex;align-items:center;gap:16px">
      <span style="width:120px;height:1px;background:var(--grey)"></span>
      <span class="display" style="font-size:18px">Blogs</span>
      <svg width="130" height="20" viewBox="0 0 130 20"><path d="M0 18H126L110 4" stroke="#8a8f95" stroke-width="1.2" fill="none"/></svg>
    </div>
  </div>
  <article class="abs post" style="left:153px">
    <div class="avatar" role="img" aria-label="Author portrait"></div>
    <div style="padding-top:10px">
      <h4>Lorem ipsum dolor sit amet</h4>
      <small>Posted by: admin &nbsp;|&nbsp; Date: Oct 12, 2013</small>
      <p>Lorem Ipsum is simply dummy text of the typesetting industry. Lorem Ipsum has been the industry's standard dummy text ever since the 1500s.</p>
    </div>
  </article>
  <div class="abs post-divider"></div>
  <article class="abs post" style="left:635px;top:2736px">
    <div class="avatar" role="img" aria-label="Author portrait"></div>
    <div style="padding-top:22px">
      <h4>Lorem ipsum dolor sit amet</h4>
      <small>Posted by: admin &nbsp;|&nbsp; Date: Oct 12, 2013</small>
      <p>Lorem Ipsum is simply dummy text of the typesetting industry. Lorem Ipsum has been the industry's standard dummy text ever since the 1500s.</p>
    </div>
  </article>
  <div class="abs btn view-all">VIEW ALL <svg width="12" height="12" viewBox="0 0 12 12"><circle cx="6" cy="6" r="6" fill="#fff"/><path d="M5 3.5L7.5 6 5 8.5" stroke="#3a3a3a" stroke-width="1.4" fill="none"/></svg></div>
</section>

<!-- footer -->
<footer>
  <div class="abs footer"></div>
  <div class="abs sitemap">
    <div class="foot-head">sitemap</div>
    <ul><li>› Home</li><li>› Product</li><li>› Contact</li><li>› Category</li><li>› Blog</li></ul>
  </div>
  <div class="abs map" role="img" aria-label="Street map showing the office location"></div>
  <div class="abs foot-brand">
    <div class="name">velqora <i></i></div>
    <div class="foot-line"><svg viewBox="0 0 14 14"><path d="M7 1a4 4 0 014 4c0 3-4 8-4 8S3 8 3 5a4 4 0 014-4z" fill="#fff"/></svg><span style="width:190px">It has roots in a piece of classical Latin literature from 45 BC</span></div>
    <div class="foot-line" style="margin-top:6px"><svg viewBox="0 0 14 14"><rect x="1" y="3" width="12" height="8" fill="#fff"/><path d="M1 3l6 5 6-5" stroke="#101010" fill="none"/></svg>info@velqora.eu</div>
    <div class="foot-phone"><svg width="18" height="18" viewBox="0 0 18 18"><path d="M4 1l3 4-2 2c1 2 3 4 5 5l2-2 4 3-2 3C8 16 2 10 1 4z" fill="#fff"/></svg> 310-482-7715</div>
  </div>
  <div class="abs follow">
    <div class="foot-head">Follow us on</div>
    <ul>
      <li><i></i>Follow us on Pagebook</li>
      <li><i></i>Follow us on Chirpline</li>
      <li><i></i>Join us on Linkwork</li>
      <li><i></i>Add us to Orbit Plus</li>
    </ul>
  </div>
  <div class="abs copy">© 2014 velqora. All rights reserved.</div>
</footer>

</body>
</html>
```